Shopping center investment profile

We need to design a two-page 8.5" x 11" brochure that can be used as a template for profiling our shopping centers and demonstrating our track record to investors.

Our company (Pelvoran Real Estate Investments) owns retail shopping centers in the southwestern United States. Our website is www.kelvistrand.example, but we will be redesigning and modernizing the website and logo in the near future, so please do not use the color schemes or framework of the website for the brochure.

Our investors are institutional and high net worth investors who typically have an existing relationship with our company. They are determining whether to invest multi-millions of dollars in a shopping center opportunity, so the brochure needs to be professional, very high quality and provide key information about the specific property.
Updates

Additional guidance on color scheme:

We would like to see a Blue (something like Hex #5A61BC) and Gold (Hex #EDB215) or (Hex #DDA24B) color scheme with some Black accents 

Thank you!

Target Market(s)

Our target audiences are institutional investors, high net-worth individuals, financial firms and medium to large commercial real estate companies.

Industry/Entity Type

Investment

Requirements
Must have
• Clean and modern look with corresponding fonts and colors.
• Incorporates the information found in the attached "Morrowick Commons profile" Pages or PDF file.
• Final file design files that can be modified easily
Nice to have
• Two examples of industry brochures are attached. These are examples of the professional quality that we are looking for, not necessarily the design or format.

```html
<!DOCTYPE html>
<html lang="en">
<head>
<meta charset="utf-8">
<title>Morrowick Commons – Property Profile</title>
<link href="https://fonts.googleapis.com/css2?family=Signika:wght@400;600;700&family=Didact+Gothic&display=swap" rel="stylesheet">
<style>
:root{
  --blue:#5a61bc;
  --blue-dark:#4a4fa8;
  --gold:#edb215;
  --gold-deep:#dda24b;
  --ink:#1c1c1c;
  --text:#555;
  --paper:#ffffff;
  --backdrop:#e9e8e6;
}
*{box-sizing:border-box;margin:0;padding:0}
html,body{width:1200px;height:836px;overflow:hidden;background:var(--backdrop)}
body{position:relative;font-family:"Didact Gothic",sans-serif;color:var(--text)}
.page{position:absolute;top:26px;width:554px;height:783px;background:var(--paper);overflow:hidden;box-shadow:0 2px 8px rgba(0,0,0,.18)}
.page--left{left:34px}
.page--right{left:614px}
.abs{position:absolute}

/* headings */
.title{font-family:"Signika",sans-serif;font-weight:700;line-height:1.05;white-space:nowrap}
.title__name{color:var(--blue);font-size:26px;display:block}
.title__sub{color:var(--gold);font-size:28px;display:block;margin-top:4px}
.section-head{font-family:"Signika",sans-serif;font-weight:600;color:var(--blue);font-size:13px;padding-bottom:2px;border-bottom:2px solid var(--gold)}

/* data panels */
.panel-tab{background:var(--blue);color:#fff;font-family:"Signika",sans-serif;font-weight:600;font-size:12.5px;padding:5px 12px;border-radius:6px 6px 0 0}
.panel{background:var(--gold);border-radius:4px;padding:6px 12px;box-shadow:1px 2px 3px rgba(0,0,0,.2)}
.panel__row{display:flex;justify-content:space-between;align-items:center;font-family:"Signika",sans-serif;font-size:8.3px;color:var(--ink);border-bottom:1px solid rgba(255,255,255,.85);height:18.4px}
.panel--invest .panel__row{height:20px}
.panel__row--plain{border-bottom:none}
.panel__total{background:#fff;color:var(--blue);font-family:"Signika",sans-serif;font-size:8.3px;border-radius:4px;padding:7px 12px;margin:6px 3px 8px}
.panel__list{list-style:none;text-align:left;line-height:1.25}
.panel__list li::before{content:"• "}

/* lists */
.dot-list{list-style:none;font-size:8.4px;line-height:1.25}
.dot-list li{position:relative;padding-left:12px;margin-bottom:9px}
.dot-list li::before{content:"";position:absolute;left:2px;top:3px;width:4px;height:4px;border-radius:50%;background:#8f93c8}
.tick-list{list-style:none;font-size:8.4px;line-height:1.25}
.tick-list li{position:relative;padding-left:16px;margin-bottom:11px}
.tick-list svg{position:absolute;left:0;top:0}

.place{font-family:"Signika",sans-serif;font-weight:600;font-size:14.5px;line-height:1.25;color:#fff;letter-spacing:.2px}
.site{font-size:10.5px;letter-spacing:1.4px;color:#fff}
.site::before{content:"";display:inline-block;width:6px;height:6px;border-radius:50%;background:var(--gold);margin-right:3px;vertical-align:middle}

/* right page */
.photo-label{font-family:"Signika",sans-serif;font-weight:600;font-size:17px;letter-spacing:.5px}
.tenant{font-family:"Signika",sans-serif;font-weight:700;font-size:14px;display:flex;align-items:center;gap:4px}
.tenant__mark{width:10px;height:10px;border-radius:50%}
.challenges{font-size:7.9px;line-height:1.27;text-align:justify}
.challenges p{position:relative;padding-left:7px;margin-bottom:8px}
.challenges p::before{content:"";position:absolute;left:0;top:3px;width:4px;height:4px;border-radius:50%;background:var(--gold)}
.challenges b{color:var(--ink);font-family:"Signika",sans-serif;font-weight:600}
.city{font-family:"Signika",sans-serif;font-weight:600;font-size:14px;color:var(--blue);letter-spacing:.3px}
</style>
</head>
<body>

<!-- PAGE ONE -->
<section class="page page--left">
  <div class="panel-tab abs" style="left:42px;top:22px;width:162px">Summary</div>
  <div class="panel abs" style="left:24px;top:47px;width:242px;height:158px">
    <div class="panel__row"><span>Property Type</span><span>Shopping Center</span></div>
    <div class="panel__row"><span>Size</span><span>79,490 sq ft</span></div>
    <div class="panel__row"><span>Purchased</span><span>April 2011</span></div>
    <div class="panel__row"><span>Total Investment</span><span>$X,XXX,XXX</span></div>
    <div class="panel__row"><span>Purchase Occupancy</span><span>8.39%</span></div>
    <div class="panel__row"><span>Current Occupancy</span><span>97.29%</span></div>
    <div class="panel__row"><span>Projected 5-year IRR (Unleveraged)</span><span>XX.XX%</span></div>
  </div>

  <div class="panel-tab abs" style="left:42px;top:222px;width:162px">Investment Information</div>
  <div class="panel panel--invest abs" style="left:24px;top:247px;width:242px;height:206px">
    <div class="panel__row"><span>Purchase Price</span><span>$X,XXX,XXX</span></div>
    <div class="panel__row"><span>Sponsor Acquisition Fee</span><span>$XX,XXX</span></div>
    <div class="panel__row"><span>Painting and Landscape</span><span>$XXX,XXX</span></div>
    <div class="panel__row"><span>TI/LC Reserve</span><span>$X,XXX,XXX</span></div>
    <div class="panel__row"><span>Operating Expenses</span><span>$XXX,XXX</span></div>
    <div class="panel__total">Total Cash Investment</div>
    <div class="panel__row panel__row--plain"><span>Investor / Sponsor Split</span><span>XX% / XX%</span></div>
    <div class="panel__row panel__row--plain" style="align-items:flex-start;height:auto;padding-top:4px">
      <span>Structure</span>
      <ul class="panel__list"><li>Cash Flow Pari Passu</li><li>Acquisition Fee</li><li>Management Fee</li></ul>
    </div>
  </div>

  <h1 class="title abs" style="left:290px;top:32px">
    <span class="title__name">Morrowick Commons</span>
    <span class="title__sub">Property Profile</span>
  </h1>

  <h2 class="section-head abs" style="left:288px;top:109px;width:243px">Opportunity</h2>
  <ul class="dot-list abs" style="left:288px;top:135px;width:240px">
    <li>Bank owned property with attractive purchase price</li>
    <li>Strong relationship with seller's broker and decision makers</li>
    <li>Redevelopment upside with management and leasing</li>
    <li>No major renovations required</li>
    <li>Tallowmere location has very strong population, education and income demographics</li>
    <li>Adjacent to premier 2,500-residence master planned community of Sorrel Lakes</li>
    <li>Strong employment area with the new Corvane Gateway hospital and the adjacent Halden Cancer center</li>
  </ul>

  <h2 class="section-head abs" style="left:288px;top:326px;width:243px">Results</h2>
  <ul class="tick-list abs" style="left:288px;top:354px;width:245px">
    <li><svg width="12" height="11" viewBox="0 0 12 11"><rect x="0.5" y="2.5" width="8" height="8" fill="none" stroke="#5a61bc"/><path d="M2 6l2.5 2.5L11 1" fill="none" stroke="#5a61bc" stroke-width="1.6"/></svg>Stabilized the shopping center within three years, producing excellent results for investors</li>
    <li><svg width="12" height="11" viewBox="0 0 12 11"><rect x="0.5" y="2.5" width="8" height="8" fill="none" stroke="#5a61bc"/><path d="M2 6l2.5 2.5L11 1" fill="none" stroke="#5a61bc" stroke-width="1.6"/></svg>Transformed the center into a vibrant destination that the surrounding community is excited about</li>
    <li><svg width="12" height="11" viewBox="0 0 12 11"><rect x="0.5" y="2.5" width="8" height="8" fill="none" stroke="#5a61bc"/><path d="M2 6l2.5 2.5L11 1" fill="none" stroke="#5a61bc" stroke-width="1.6"/></svg>Transitioned legacy tenants to upgrade the business operators</li>
    <li><svg width="12" height="11" viewBox="0 0 12 11"><rect x="0.5" y="2.5" width="8" height="8" fill="none" stroke="#5a61bc"/><path d="M2 6l2.5 2.5L11 1" fill="none" stroke="#5a61bc" stroke-width="1.6"/></svg>Reduced the shopping center's operating expenses by replacing vendors and appealing property taxes</li>
  </ul>

  <svg class="abs" style="left:0;top:460px" width="554" height="323" viewBox="0 0 554 323">
    <defs>
      <linearGradient id="render-left" x1="0" y1="0" x2="0" y2="1">
        <stop offset="0" stop-color="#8fb8e6"/>
        <stop offset=".45" stop-color="#dfe9f4"/>
        <stop offset=".62" stop-color="#c9915e"/>
        <stop offset=".85" stop-color="#9a8a7a"/>
        <stop offset="1" stop-color="#b9b6b0"/>
      </linearGradient>
    </defs>
    <path role="img" aria-label="Architectural rendering of the renovated storefronts with signage bands, trees and parked cars" d="M0,55 C150,20 350,10 554,35 L554,290 L0,290 Z" fill="url(#render-left)"/>
    <path d="M0,42 C180,2 380,-4 554,26 L554,36 C380,8 180,14 0,64 Z" fill="#5a61bc"/>
    <path d="M0,262 C200,232 400,236 554,272 L554,284 C400,250 200,246 0,280 Z" fill="#edb215"/>
    <path d="M0,282 C200,252 400,256 554,288 L554,323 L0,323 Z" fill="#5a61bc"/>
  </svg>
  <p class="place abs" style="left:56px;top:742px">SWC OF MORROW RD AND<br>KESTREL RD TALLOWMERE, ARIZONA</p>
  <p class="site abs" style="left:392px;top:762px">www.kelvistrand.example</p>
</section>

<!-- PAGE TWO -->
<section class="page page--right">
  <svg class="abs" style="left:0;top:0" width="554" height="430" viewBox="0 0 554 430">
    <defs>
      <linearGradient id="render-after" x1="0" y1="0" x2="0" y2="1">
        <stop offset="0" stop-color="#8fb8e6"/>
        <stop offset=".4" stop-color="#dfe9f4"/>
        <stop offset=".6" stop-color="#c9915e"/>
        <stop offset=".82" stop-color="#8a7f78"/>
        <stop offset="1" stop-color="#a9a7a3"/>
      </linearGradient>
      <linearGradient id="photo-before" x1="0" y1="0" x2="0" y2="1">
        <stop offset="0" stop-color="#a8c6e8"/>
        <stop offset=".5" stop-color="#e6ecf2"/>
        <stop offset=".7" stop-color="#b99575"/>
        <stop offset="1" stop-color="#8e8b86"/>
      </linearGradient>
    </defs>
    <path d="M0,110 C10,115 20,125 30,140 L0,150 Z" fill="#5a61bc"/>
    <path d="M346,118 C420,110 490,110 554,90 L554,100 C490,122 420,122 346,124 Z" fill="#5a61bc"/>
    <path role="img" aria-label="After: rendering of the repainted shopping center with new signage, parking lot and cars" d="M0,160 C150,150 330,140 554,112 L554,380 C350,360 150,380 0,400 Z" fill="url(#render-after)"/>
    <path d="M0,420 C180,380 380,372 554,385 L554,392 C380,380 180,388 0,426 Z" fill="#edb215"/>
    <path d="M0,400 C150,380 350,362 554,380 L554,386 C380,374 180,382 0,422 Z" fill="#fff"/>
    <ellipse role="img" aria-label="Before: photo of the original center with faded facade and empty parking lot" cx="185" cy="138" rx="120" ry="110" fill="url(#photo-before)" stroke="#fff" stroke-width="4"/>
  </svg>
  <span class="photo-label abs" style="left:80px;top:89px;color:var(--ink)">BEFORE</span>
  <span class="photo-label abs" style="left:464px;top:185px;color:#fff">AFTER</span>

  <h1 class="title abs" style="right:30px;top:34px;text-align:right">
    <span class="title__name" style="font-size:25px">Morrowick Commons</span>
    <span class="title__sub" style="font-size:26px;margin-top:2px">Property Profile</span>
  </h1>

  <div class="tenant abs" style="left:14px;top:442px;color:#7a3fa0"><span class="tenant__mark" style="background:var(--gold)"></span>Pinwheel Play</div>
  <div class="tenant abs" style="left:140px;top:432px;color:#d12a86">Saguaro Grill</div>
  <div class="tenant abs" style="left:245px;top:475px;color:#4a86c5;font-weight:400"><span class="tenant__mark" style="background:#4a86c5"></span>Quillberry</div>

  <div role="img" aria-label="Site plan showing tenant pads, parking layout and adjacent roads" class="abs" style="left:10px;top:510px;width:342px;height:224px;background:linear-gradient(135deg,#b8bcc0,#a4c98a 60%,#c9cccf)"></div>

  <h2 class="section-head abs" style="left:372px;top:418px;width:162px">Challenges and Solutions</h2>
  <div class="challenges abs" style="left:372px;top:445px;width:160px">
    <p><b>Nationwide vacancy rate</b> - Pelvoran did significant due diligence on the property before purchasing the asset, and determined that the location is an A/A-; Tenant improvement and leasing commissions were reserved in order to attract national and regional tenants</p>
    <p><b>Size of Anchor space</b> - Pelvoran determined that a family-friendly entertainment venue would best serve the demographics in the area instead of another grocer; Pelvoran sought out an experienced operator in Pinwheel Play, who has multiple locations in three states</p>
    <p><b>Curb Appeal</b> - With vacancy and a stigma attached to the center, Pelvoran had to change the center's appeal to the community. Pelvoran worked hand in hand with the Town of Tallowmere and the Sorrel Lakes community association to paint the center, upgrade landscaping and add new and larger monument signs</p>
  </div>

  <svg class="abs" style="left:0;top:720px" width="554" height="63" viewBox="0 0 554 63">
    <path d="M340,40 C420,22 490,18 554,24 L554,30 C490,24 420,28 340,40 Z" fill="#edb215"/>
    <path d="M150,63 C300,50 450,44 554,40 L554,63 Z" fill="#5a61bc"/>
  </svg>
  <p class="city abs" style="left:21px;top:755px">TALLOWMERE, ARIZONA</p>
  <p class="site abs" style="left:392px;top:762px">www.kelvistrand.example</p>
</section>

</body>
</html>
```